VelloTask Business Card

Our company is called VelloTask and we are based in Tel Aviv, Israel. We create innovative and exciting methods for getting people on the web engaged with content. We need a cool yet professional business card that will represent our management level employees. keep in mind this is a start up company with a young atmosphere. You can be inspired by our logo (file attached, make sure you have the right font "Ubuntu-Condensed") Use the colors that are used in the logo and create a colourful and professional business card.

```html
<!DOCTYPE html>
<html lang="en">
<head>
<meta charset="utf-8">
<title>VelloTask Business Card</title>
<link href="https://fonts.googleapis.com/css2?family=Ubuntu:wght@400;500&family=Ubuntu+Condensed&family=Open+Sans:wght@400;600&display=swap" rel="stylesheet">
<style>
  :root {
    --stage: #d9d4cf;
    --card-white: #ffffff;
    --card-grey: #efefef;
    --ink: #1d1d1d;
    --purple: #8e2a8c;
    --pink: #e9287a;
    --yellow: #fdd20e;
    --blue: #5ab4de;
    --green: #8dc63f;
    --orange: #f7a941;
    --brand-blue: #1e88c9;
  }
  html, body {
    margin: 0;
    width: 1200px;
    height: 1200px;
    overflow: hidden;
    background: var(--stage);
  }
  .canvas {
    position: relative;
    width: 1200px;
    height: 1200px;
  }
  .card {
    position: absolute;
    left: 120px;
    width: 960px;
    height: 560px;
    background: var(--card-white);
    overflow: hidden;
    box-shadow: 0 6px 18px rgba(0,0,0,0.25);
  }
  .card-front { top: 22px; background: var(--card-grey); }
  .card-back { top: 614px; }
  .card-art {
    position: absolute;
    inset: 0;
    width: 960px;
    height: 560px;
  }
  .name-band {
    position: absolute;
    left: 50px;
    top: 62px;
    width: 380px;
    padding: 8px 14px 10px;
    background: linear-gradient(90deg, rgba(255,255,255,0.9), rgba(255,255,255,0.35));
  }
  .person-name {
    margin: 0;
    font-family: "Open Sans", Arial, sans-serif;
    font-weight: 600;
    font-size: 31px;
    line-height: 1.1;
    color: var(--ink);
  }
  .person-title {
    margin: 4px 0 0;
    font-family: "Open Sans", Arial, sans-serif;
    font-size: 27px;
    line-height: 1.1;
    color: var(--purple);
  }
  .contact-list {
    position: absolute;
    left: 50px;
    top: 326px;
    margin: 0;
    padding: 0;
    list-style: none;
    font-family: "Open Sans", Arial, sans-serif;
    font-size: 23px;
    color: var(--ink);
  }
  .contact-list li {
    display: flex;
    align-items: center;
    height: 44px;
  }
  .contact-icon {
    width: 22px;
    height: 22px;
    margin-right: 14px;
    fill: var(--purple);
  }
  .brand {
    position: absolute;
    display: flex;
    align-items: center;
    gap: 16px;
  }
  .brand-dot {
    border-radius: 50%;
    background: var(--brand-blue);
  }
  .brand-name {
    font-family: "Ubuntu Condensed", "Ubuntu", sans-serif;
    color: var(--ink);
    line-height: 1;
    letter-spacing: 1px;
  }
  .card-front .brand { right: 40px; top: 236px; }
  .card-front .brand-dot { width: 36px; height: 36px; }
  .card-front .brand-name { font-size: 72px; }
  .card-back .brand { left: 50%; top: 320px; transform: translateX(-50%); }
  .card-back .brand-dot { width: 38px; height: 38px; }
  .card-back .brand-name { font-size: 80px; }
</style>
</head>
<body>
<main class="canvas">

  <section class="card card-front">
    <svg class="card-art" viewBox="0 0 960 560" aria-hidden="false">
      <defs>
        <linearGradient id="confettiFront" x1="0" y1="0" x2="1" y2="1">
          <stop offset="0" stop-color="#e9287a" stop-opacity="0.55"/>
          <stop offset="0.3" stop-color="#fdd20e" stop-opacity="0.55"/>
          <stop offset="0.55" stop-color="#5ab4de" stop-opacity="0.55"/>
          <stop offset="0.8" stop-color="#8e2a8c" stop-opacity="0.5"/>
          <stop offset="1" stop-color="#8dc63f" stop-opacity="0.5"/>
        </linearGradient>
        <linearGradient id="confettiCorner" x1="0" y1="0" x2="1" y2="1">
          <stop offset="0" stop-color="#f7a941" stop-opacity="0.55"/>
          <stop offset="0.4" stop-color="#e9287a" stop-opacity="0.5"/>
          <stop offset="0.7" stop-color="#5ab4de" stop-opacity="0.55"/>
          <stop offset="1" stop-color="#8e2a8c" stop-opacity="0.5"/>
        </linearGradient>
      </defs>
      <path class="wave-panel" fill="#ffffff"
            d="M0 0 H610 C560 40 600 120 520 200 C440 280 340 250 200 300 C120 330 60 370 0 410 Z"/>
      <path role="img" aria-label="Cluster of colourful confetti dots" fill="url(#confettiFront)"
            d="M0 0 H570 C540 60 560 130 470 190 C390 240 300 230 200 270 C130 300 70 340 0 370 Z"/>
      <circle class="corner-panel" cx="940" cy="590" r="300" fill="#ffffff"/>
      <path role="img" aria-label="Cluster of colourful confetti dots" fill="url(#confettiCorner)"
            d="M960 320 C860 330 760 380 700 460 C670 500 660 530 655 560 H960 Z"/>
    </svg>

    <div class="name-band">
      <p class="person-name">Your name here</p>
      <p class="person-title">Title here</p>
    </div>

    <div class="brand">
      <span class="brand-dot"></span>
      <span class="brand-name">VelloTask</span>
    </div>

    <ul class="contact-list">
      <li>
        <svg class="contact-icon" viewBox="0 0 24 24"><path d="M12 2 L1 12 H4 V22 H10 V15 H14 V22 H20 V12 H23 Z"/></svg>
        Address line 1,Address line 2,Address line 3
      </li>
      <li>
        <svg class="contact-icon" viewBox="0 0 24 24"><path d="M2 7 C2 3 22 3 22 7 V9 H17 V7 H7 V9 H2 Z M5 10 H19 L21 21 H3 Z"/><rect x="7" y="13" width="2" height="2" fill="#fff"/><rect x="11" y="13" width="2" height="2" fill="#fff"/><rect x="15" y="13" width="2" height="2" fill="#fff"/><rect x="7" y="17" width="2" height="2" fill="#fff"/><rect x="11" y="17" width="2" height="2" fill="#fff"/><rect x="15" y="17" width="2" height="2" fill="#fff"/></svg>
        (000)5644.566
      </li>
      <li>
        <svg class="contact-icon" viewBox="0 0 24 24"><path d="M6 2 H16 L18 4 V9 H6 Z M2 10 H22 V19 H18 V15 H6 V19 H2 Z M7 16 H17 V22 H7 Z"/></svg>
        (000)5644.566
      </li>
    </ul>
  </section>

  <section class="card card-back">
    <svg class="card-art" viewBox="0 0 960 560">
      <defs>
        <linearGradient id="confettiTopLeft" x1="0" y1="0" x2="1" y2="1">
          <stop offset="0" stop-color="#f7a941" stop-opacity="0.55"/>
          <stop offset="0.35" stop-color="#8e2a8c" stop-opacity="0.5"/>
          <stop offset="0.65" stop-color="#8dc63f" stop-opacity="0.5"/>
          <stop offset="1" stop-color="#5ab4de" stop-opacity="0.55"/>
        </linearGradient>
        <linearGradient id="confettiBottomRight" x1="0" y1="0" x2="1" y2="1">
          <stop offset="0" stop-color="#5ab4de" stop-opacity="0.55"/>
          <stop offset="0.4" stop-color="#8dc63f" stop-opacity="0.5"/>
          <stop offset="0.7" stop-color="#fdd20e" stop-opacity="0.55"/>
          <stop offset="1" stop-color="#e9287a" stop-opacity="0.5"/>
        </linearGradient>
      </defs>
      <path role="img" aria-label="Cluster of colourful confetti dots" fill="url(#confettiTopLeft)"
            d="M0 0 H290 C270 70 220 130 160 170 C110 205 50 220 0 240 Z"/>
      <path role="img" aria-label="Cluster of colourful confetti dots" fill="url(#confettiBottomRight)"
            d="M960 300 C880 320 800 370 740 430 C700 470 680 520 670 560 H960 Z"/>
    </svg>

    <div class="brand">
      <span class="brand-dot"></span>
      <span class="brand-name">VelloTask</span>
    </div>
  </section>

</main>
</body>
</html>
```